PostCard Design Project

We are a landscaping business and offer Landscaping services: Design • Paving and Concreting styles • Pool Copings • Retaining Walls • Plant Supply • Decking • Pergolas • Water Features • Irrigation • Instant Turf • Synthetic Turf Surfaces • and more...

We are looking to create a Postcard - this will be used when we are working on a project and will be dropped into letterboxes of the residents neighbouring the project address. It should be along the lines of: "We apologise for any disturbance you may incur while we are working on your neighbours property." It should also include a 10% discount offer for any services they would like to get done, maybe on the back,, along the lines of" While we are in your area we'd like to offer you a 10% discount on any of our landscaping services" Offer valid for 30 days only. Also maybe a list of servcies on the back as well.

Industry/Entity Type

Landscaping

Requirements
Must have
• Company Logo, and contact details

```html
<!DOCTYPE html>
<html lang="en">
<head>
<meta charset="utf-8">
<title>Fernvale Landscapes – Neighbour Postcard</title>
<link href="https://fonts.googleapis.com/css2?family=Arimo:wght@400;700&display=swap" rel="stylesheet">
<style>
  :root {
    --backdrop: #ecebe8;
    --card: #ffffff;
    --panel: #e6e6e7;
    --green: #8cc63f;
    --green-dark: #6fa52c;
    --ink: #231f20;
    --slate: #3d4b57;
    --rule: #3a3a3a;
  }
  * { margin: 0; padding: 0; box-sizing: border-box; }
  html, body { width: 990px; height: 1200px; overflow: hidden; }
  body {
    background: var(--backdrop);
    font-family: "Arimo", Arial, sans-serif;
    color: var(--ink);
    position: relative;
  }
  .card {
    position: absolute;
    left: 163px;
    width: 664px;
    height: 473px;
    background: var(--card);
    box-shadow: 0 2px 6px rgba(0,0,0,.18);
    overflow: hidden;
  }
  /* Front */
  .card--front { top: 92px; }
  .front__photo {
    position: absolute; left: 0; top: 0; width: 664px; height: 351px;
    background: linear-gradient(160deg, #8fb56a 0%, #6f9a45 40%, #8a7350 70%, #5d4a35 100%);
  }
  .front__headline-box {
    position: absolute; left: 240px; top: 338px; width: 424px; height: 50px;
    background: var(--card);
  }
  .front__headline {
    position: absolute; left: 247px; top: 340px;
    font-size: 47px; font-weight: 700; color: var(--green); letter-spacing: 0.5px;
  }
  .front__message {
    position: absolute; right: 26px; top: 398px; text-align: right;
    font-size: 17.5px; font-weight: 700; line-height: 26px;
  }
  .brand {
    position: absolute; display: flex; align-items: center; gap: 10px;
    font-weight: 700; color: var(--green);
  }
  .brand__dot { border-radius: 50%; background: var(--green); flex: none; }
  .front__brand { left: 22px; top: 378px; font-size: 30px; }
  .front__brand .brand__dot { width: 34px; height: 34px; }

  /* Back */
  .card--back { top: 635px; }
  .back__panel {
    position: absolute; left: 0; top: 0; width: 363px; height: 473px; background: var(--panel);
  }
  .back__brand { left: 28px; top: 52px; font-size: 38px; }
  .back__brand .brand__dot { width: 46px; height: 46px; }
  .services {
    position: absolute; top: 181px; list-style: none;
    font-size: 13px; line-height: 18.4px;
  }
  .services li::before {
    content: ""; display: inline-block; width: 5px; height: 5px; border-radius: 50%;
    background: var(--green); margin-right: 6px; vertical-align: 2px;
  }
  .services--one { left: 27px; }
  .services--two { left: 144px; }
  .offer { position: absolute; left: 28px; top: 318px; width: 322px; height: 128px; }
  .offer svg { position: absolute; inset: 0; }
  .offer__title {
    position: absolute; left: 125px; top: 22px;
    font-size: 31px; font-weight: 700; color: var(--green);
  }
  .offer__text {
    position: absolute; left: 125px; top: 82px; width: 150px;
    font-size: 7.5px; line-height: 9px; color: #ffffff;
  }
  .offer__fine {
    position: absolute; left: 125px; top: 110px; font-size: 5.5px; color: var(--ink);
  }
  .return-address {
    position: absolute; right: 135px; top: 74px; text-align: right;
    font-size: 12.5px; line-height: 19px;
  }
  .return-address strong { font-weight: 700; }
  .stamp {
    position: absolute; left: 548px; top: 39px; width: 91px; height: 121px;
    border: 1.5px solid var(--rule);
  }
  .address-lines { position: absolute; left: 402px; top: 200px; width: 236px; }
  .address-lines span {
    display: block; height: 29px; border-bottom: 1.5px solid var(--rule);
  }
  .address-lines span:first-child { height: 1px; }
  .contact {
    position: absolute; left: 363px; width: 301px; top: 370px; text-align: center;
  }
  .contact__label { font-size: 13px; }
  .contact__phone {
    display: flex; align-items: center; justify-content: center; gap: 10px;
    font-size: 23px; font-weight: 700; margin-top: 3px;
  }
  .contact__or { font-size: 13px; margin-top: 2px; }
  .contact__web { font-size: 16px; margin-top: 3px; }
  .contact__web b { font-weight: 700; }
</style>
</head>
<body>

<section class="card card--front">
  <div class="front__photo" role="img" aria-label="Photo of a landscaper kneeling and rolling out fresh instant turf beside a paved path"></div>
  <div class="front__headline-box"></div>
  <h1 class="front__headline">WE APOLOGISE</h1>
  <p class="front__message">for any disturbance you may incur while we<br>are working on your neighbours property.</p>
  <div class="brand front__brand"><span class="brand__dot"></span>Fernvale</div>
</section>

<section class="card card--back">
  <div class="back__panel"></div>
  <div class="brand back__brand"><span class="brand__dot"></span>Fernvale</div>

  <ul class="services services--one">
    <li>Design</li><li>Pergolas</li><li>Water Features</li>
    <li>Irrigation</li><li>Instant Turf</li><li>Plant Supply</li>
  </ul>
  <ul class="services services--two">
    <li>Decking</li><li>Pool Copings</li><li>Retaining Walls</li>
    <li>Synthetic Turf Surfaces</li><li>Paving and Concreting styles</li><li>and more...</li>
  </ul>

  <div class="offer">
    <svg width="322" height="128" viewBox="0 0 322 128" aria-hidden="true">
      <defs>
        <clipPath id="offer-shape">
          <path d="M10 0 H282 L320 46 Q322 48 320 52 L282 128 H10 Q0 128 0 118 V10 Q0 0 10 0 Z"/>
        </clipPath>
      </defs>
      <g clip-path="url(#offer-shape)">
        <rect width="322" height="128" fill="#3d4b57"/>
        <rect y="100" width="322" height="28" fill="#8cc63f"/>
      </g>
      <circle cx="55" cy="64" r="46" fill="#8cc63f"/>
      <circle cx="55" cy="64" r="30" fill="#3d4b57"/>
    </svg>
    <div class="offer__title">10% OFF</div>
    <p class="offer__text">While we are in your area we'd like to offer you a discount on any of our landscaping services*.</p>
    <p class="offer__fine">*Offer valid for 30 days only.</p>
  </div>

  <address class="return-address" style="font-style:normal">
    <strong>Fernvale Landscapes Pty Ltd</strong><br>
    Suite 4/27 Garden Rd.<br>
    Greenbrook, Vic. 3999
  </address>
  <div class="stamp"></div>

  <div class="address-lines"><span></span><span></span><span></span><span></span><span></span><span></span></div>

  <div class="contact">
    <p class="contact__label">Call Us</p>
    <p class="contact__phone">
      <svg width="30" height="30" viewBox="0 0 30 30" aria-hidden="true">
        <circle cx="15" cy="15" r="13.5" fill="none" stroke="#231f20" stroke-width="2"/>
        <path d="M10 8 l3 0 l1.5 4 l-2 1.5 q1.5 3.5 4 4 l1.5 -2 l4 1.5 l0 3 q-1 1.5 -3 1.5 q-7 -1 -10 -9 q0 -3 1 -4.5 z" fill="#231f20"/>
      </svg>
      (03) 5550 0123
    </p>
    <p class="contact__or">or visit</p>
    <p class="contact__web">www.<b>fernvalelandscapes</b>.com.au</p>
  </div>
</section>

</body>
</html>
```